I would like a stylish low key card that represents my Cedar Lodge. A boutique rental property . This property is of the highest standard and I wish the card to covey this without being old fashion

Industry/Entity Type

Boutique

Contact Information for Business Card

Tess Varlowe
0438207519
tess.varlowe@varlowe.com.au Cedar Lodge

```html
<!DOCTYPE html>
<html lang="en">
<head>
<meta charset="utf-8">
<title>Cedar Lodge – Business Card</title>
<link rel="stylesheet" href="https://fonts.googleapis.com/css2?family=Abril+Fatface&family=PT+Serif&display=swap">
<style>
  :root {
    --paper: #ffffff;
    --crimson: #ba3540;
    --olive: #585c48;
    --ink-light: #ffffff;
  }
  html, body {
    margin: 0;
    padding: 0;
    overflow: hidden;
    background: var(--paper);
  }
  .card {
    position: relative;
    width: 1200px;
    height: 693px;
    overflow: hidden;
    background: var(--paper);
  }
  .card__disc {
    position: absolute;
    inset: 0;
    width: 1200px;
    height: 693px;
  }
  .card__disc circle {
    fill: var(--crimson);
  }
  .brand {
    position: absolute;
    left: 30px;
    top: 110px;
    margin: 0;
    font-family: "PT Serif", serif;
    font-weight: 400;
    font-size: 96px;
    line-height: 128px;
    color: var(--olive);
  }
  .brand__line {
    display: block;
  }
  .brand__line--the { padding-left: 10px; }
  .brand__line--first { padding-left: 90px; }
  .brand__line--second { padding-left: 30px; }
  .contact {
    position: absolute;
    right: 62px;
    top: 236px;
    text-align: right;
    color: var(--ink-light);
  }
  .contact__name {
    margin: 0;
    font-family: "Abril Fatface", serif;
    font-weight: 400;
    font-size: 56px;
    line-height: 70px;
  }
  .contact__phone,
  .contact__email {
    margin: 0;
    font-family: "PT Serif", serif;
    font-weight: 400;
  }
  .contact__phone {
    font-size: 50px;
    line-height: 68px;
    margin-right: 12px;
  }
  .contact__email {
    font-size: 41px;
    line-height: 62px;
    margin-right: 12px;
  }
</style>
</head>
<body>
  <div class="card">
    <svg class="card__disc" viewBox="0 0 1200 693" aria-hidden="true">
      <circle cx="1082" cy="344" r="680"/>
    </svg>

    <h1 class="brand">
      <span class="brand__line brand__line--the">The</span>
      <span class="brand__line brand__line--first">Cedar</span>
      <span class="brand__line brand__line--second">Lodge</span>
    </h1>

    <div class="contact">
      <p class="contact__name">Tess Varlowe</p>
      <p class="contact__phone">tel: 0438207519</p>
      <p class="contact__email">tess.varlowe@varlowe.com.au</p>
    </div>
  </div>
</body>
</html>
```